Lorne Hollow Farm Postcard Design

I am looking for a new postcard design to mail out this season. We are a Farm business that does wholesale and retail and bulk seasoned firewood sales. we sell firewood from anything from bagged wood to tractor trailer loads of wood. We sell firewood in bulk bags. Pick up or delivery available there is no order to big or too small. I need my business name and phone number on the cards Lorne Hollow Farm 848-316-0572 (call or text) I would like it to say we are the best priced guaranteed. I want something that is simple and straight forward but also really catches the eye when they see these in the mail box. I attached my logo and feel free to use photos of split firewood if you would like. id like my email on the card Lornehollowfarm90@mailvista.net.

Target Market(s)

Firewood purchasers

Industry/Entity Type

agriculture

Requirements
Must have
• email phone number logo

```html
<!DOCTYPE html>
<html lang="en">
<head>
<meta charset="UTF-8">
<title>Lorne Hollow Farm Postcard</title>
<link href="https://fonts.googleapis.com/css2?family=Poppins:wght@300;600;700&display=swap" rel="stylesheet">
<style>
  :root{
    --stage:#a9a9a9;
    --ink:#000000;
    --paper:#ffffff;
    --line:#1a1a1a;
    --orange:#f26522;
    --amber:#fdb813;
    --photo-sky:#6f7f8c;
    --photo-ground:#3a4438;
  }
  *{margin:0;padding:0;box-sizing:border-box}
  html,body{width:1199px;height:1200px;overflow:hidden;background:var(--stage);font-family:"Poppins",sans-serif}
  .card{position:absolute;left:204px;width:790px;height:526px;overflow:hidden}
  .card--front{top:44px;background:var(--ink)}
  .card--back{top:627px;background:var(--paper)}
  .photo-area{position:absolute;inset:0;width:100%;height:100%;
    background:linear-gradient(90deg,rgba(0,0,0,0) 0%,rgba(0,0,0,.15) 30%,rgba(0,0,0,.85) 50%,var(--ink) 62%),
               linear-gradient(180deg,var(--photo-sky) 0%,#55635d 45%,var(--photo-ground) 75%,#8a8a80 100%)}
  .headline{position:absolute;color:var(--paper);font-weight:700;text-transform:uppercase;letter-spacing:.5px}
  .card--front .headline{left:56px;top:118px;font-size:71px;line-height:67px}
  .card--back .headline{left:50px;top:180px;font-size:55px;line-height:45px}
  .brand{position:absolute;color:var(--orange);font-weight:700;text-align:center;line-height:1.1}
  .card--front .brand{left:584px;top:92px;width:160px;font-size:22px}
  .card--back .brand{left:48px;top:56px;width:130px;font-size:19px}
  .phone{position:absolute;color:var(--paper);font-weight:700;font-size:27px;letter-spacing:.5px}
  .email{position:absolute;color:var(--paper);font-weight:300;font-size:15px}
  .card--front .phone{left:507px;top:398px}
  .card--front .email{left:494px;top:437px}
  .card--back .phone{left:50px;top:410px}
  .card--back .email{left:50px;top:450px}
  .badge{position:absolute;left:530px;top:216px;width:144px;height:144px}
  .badge-text{position:absolute;left:530px;top:264px;width:144px;text-align:center;color:var(--paper);font-weight:600;font-size:14px;line-height:17px;transform:rotate(-8deg)}
  .back-shapes{position:absolute;inset:0}
  .stamp-box{position:absolute;left:625px;top:54px;width:109px;height:122px;border:1.5px solid var(--line)}
  .address-line{position:absolute;left:442px;width:291px;border-top:1.5px solid var(--line)}
</style>
</head>
<body>
  <section class="card card--front">
    <div class="photo-area" role="img" aria-label="Photo of a green forestry tractor loaded with logs in a yard under a blue sky"></div>
    <div class="brand">Lorne Hollow Farm</div>
    <h1 class="headline">Bulk<br>Seasoned<br>Firewood<br>Sales</h1>
    <svg class="badge" viewBox="0 0 100 100" aria-hidden="true">
      <defs>
        <linearGradient id="badgeFill" x1="0" y1="1" x2="1" y2="0">
          <stop offset="0" stop-color="#f26522"/><stop offset="1" stop-color="#fdb813"/>
        </linearGradient>
      </defs>
      <polygon fill="url(#badgeFill)" points="50,4 59,14 72,9 75,22 89,25 85,38 96,47 86,57 91,70 78,74 75,88 62,85 52,96 42,87 29,92 25,79 12,75 16,62 5,52 15,42 10,29 23,25 27,12 40,16"/>
    </svg>
    <div class="badge-text">Best Price<br>Guaranteed</div>
    <div class="phone">848-316-0572</div>
    <div class="email">Lornehollowfarm90@mailvista.net</div>
  </section>

  <section class="card card--back">
    <svg class="back-shapes" viewBox="0 0 633 421" preserveAspectRatio="none" width="790" height="526" aria-hidden="true">
      <defs>
        <linearGradient id="wedgeFill" x1="0" y1="1" x2="1" y2="0">
          <stop offset="0" stop-color="#f26522"/><stop offset="1" stop-color="#fdb813"/>
        </linearGradient>
      </defs>
      <polygon fill="#000" points="0,0 365,0 277,421 0,421"/>
      <polygon fill="url(#wedgeFill)" points="262,0 365,0 315,243"/>
    </svg>
    <div class="brand">Lorne Hollow Farm</div>
    <h2 class="headline">Bulk<br>Seasoned<br>Firewood<br>Sales</h2>
    <div class="phone">848-316-0572</div>
    <div class="email">Lornehollowfarm90@mailvista.net</div>
    <div class="stamp-box"></div>
    <div class="address-line" style="top:320px"></div>
    <div class="address-line" style="top:377px"></div>
    <div class="address-line" style="top:435px"></div>
  </section>
</body>
</html>
```